Packaging Design for "Out-beyond" healthy snack

We are a young trading company based in Melaka, Malaysia. Our product range include healthy snack food products such as;
1. Dried fruit (Raisin, Date and Apricot)
2. Nuts (Almond, walnut and Pitstachio)

Our Brand name is - Out-Beyond (registrated mark)
Motto: Healthy snacks that everyone will craved out-Beyond meal time.

Target market segment:
1. Night life business such as Pub, Lounge, Kara-oke
2. Vegetarian and Health food restaurant
3. Appetiser for Premium Restaurant

Packs size : 100g, 250g and 500g

Packing type: Screw Cap Jar (Square L7.5cm X W7.5cm X H9.0cm)

Competitor website:
http://www.brolvexa.com/index.php?ws=ourproducts&cat=Nuts#openproducts

https://kelpo.com/driedfruit/ (For company philosophy)

TRWalsby
trwalsby@mailvexo.com

Ortivel Grove (M) Sdn. Bhd. (owner of Out-beyond brand)

Target Market(s)

Customer that have middle and high income that have disposable budget for healthy and good taste snack in between meal time. Those business man that like to meet client at the night life outlets would enjoy our snacks

Industry/Entity Type

It Company

Font styles to use
Sans Serif

Colors
faa54b
886aae
87cfc6

Requirements
Must have
• 1. Out-beyond as brand name
• 2. Product names area
• 3. Die cut window that let consumer see the product inside
• 4. Nutritional facts and Ingredients
Nice to have
• 1. A attractive logo for "Out-beyond" brand

```html
<!DOCTYPE html>
<html lang="en">
<head>
<meta charset="utf-8">
<title>Out-Beyond Premium Snack Labels</title>
<link rel="stylesheet" href="https://fonts.googleapis.com/css2?family=Staatliches&family=Oswald:wght@400;500&display=swap">
<style>
  :root {
    --canvas: #ffffff;
    --label-black: #050505;
    --teal: #87cfc6;
    --orange: #faa54b;
    --purple: #886aae;
    --taupe: #9d8b7f;
    --white: #ffffff;
    --badge-text: #b9824f;
  }
  * { margin: 0; padding: 0; box-sizing: border-box; }
  html, body { width: 1000px; height: 1200px; overflow: hidden; background: var(--canvas); }
  .canvas { position: relative; width: 1000px; height: 1200px; background: var(--canvas); }

  .label {
    position: absolute;
    width: 347px;
    height: 339px;
    background: var(--label-black);
    overflow: hidden;
    --accent: var(--teal);
  }
  .label--almonds { left: 93px; top: 188px; --accent: var(--teal); }
  .label--mixed   { left: 565px; top: 188px; --accent: var(--orange); }
  .label--fruits  { left: 93px; top: 783px; --accent: var(--purple); }
  .label--peanuts { left: 565px; top: 783px; --accent: var(--taupe); }

  .brand-mark {
    position: absolute;
    left: 0;
    top: 6px;
    width: 100%;
    display: flex;
    justify-content: center;
    align-items: center;
    gap: 7px;
    color: var(--accent);
    font-family: "Oswald", sans-serif;
    font-weight: 400;
    font-size: 15px;
    line-height: 18px;
    letter-spacing: 0.4px;
  }
  .brand-mark__square {
    width: 8px;
    height: 8px;
    background: var(--accent);
  }

  .grade {
    position: absolute;
    top: 61px;
    left: 0;
    width: 100%;
    display: flex;
    justify-content: center;
    align-items: center;
    gap: 8px;
    color: var(--accent);
    font-family: "Oswald", sans-serif;
    font-weight: 500;
    font-size: 8px;
    letter-spacing: 3px;
  }
  .grade::before, .grade::after {
    content: "";
    width: 52px;
    height: 1px;
    background: var(--accent);
  }

  .product-name {
    position: absolute;
    top: 74px;
    left: 0;
    width: 100%;
    text-align: center;
    color: var(--accent);
    font-family: "Staatliches", sans-serif;
    font-weight: 400;
    font-size: 42px;
    letter-spacing: 2px;
    line-height: 46px;
    word-spacing: 8px;
  }

  .window { position: absolute; left: 0; top: 0; width: 347px; height: 339px; }

  .badge {
    position: absolute;
    width: 48px;
    height: 48px;
    border-radius: 50%;
    background: var(--label-black);
    color: var(--badge-text);
    font-family: "Staatliches", sans-serif;
    font-size: 14px;
    line-height: 13px;
    display: flex;
    flex-direction: column;
    align-items: center;
    justify-content: center;
    transform: rotate(18deg);
  }
  .badge--healthy { left: 82px; top: 152px; }
  .badge--natural { left: 146px; top: 172px; }
  .badge--organic { left: 210px; top: 197px; }

  .net-weight {
    position: absolute;
    left: 311px;
    top: 202px;
    color: var(--accent);
    font-family: "Staatliches", sans-serif;
    font-size: 11px;
    letter-spacing: 0.5px;
  }

  .tagline {
    position: absolute;
    left: 12px;
    top: 279px;
    color: var(--white);
    font-family: "Oswald", sans-serif;
    font-size: 8px;
    line-height: 12px;
    letter-spacing: 0.6px;
    text-transform: uppercase;
  }
  .tagline .quote-mark {
    position: absolute;
    left: -4px;
    top: -3px;
    font-family: "Staatliches", sans-serif;
    font-size: 16px;
  }
  .tagline p { padding-left: 4px; }
</style>
</head>
<body>
<main class="canvas">

  <section class="label label--almonds">
    <svg class="window" viewBox="0 0 347 339" role="img" aria-label="Die-cut window showing whole almonds inside the jar">
      <defs>
        <linearGradient id="almond-fill" x1="0" y1="0" x2="1" y2="1">
          <stop offset="0" stop-color="#b8743c"/>
          <stop offset="0.5" stop-color="#a0592a"/>
          <stop offset="1" stop-color="#c98a4f"/>
        </linearGradient>
      </defs>
      <polygon points="0,132 347,234 347,339 0,339" fill="url(#almond-fill)"/>
    </svg>
    <div class="brand-mark"><span class="brand-mark__square"></span><span>Out-Beyond</span></div>
    <div class="grade">PREMIUM</div>
    <h2 class="product-name">Almonds</h2>
    <div class="badge badge--healthy"><span>HEA</span><span>LTHY</span></div>
    <div class="badge badge--natural"><span>NAT</span><span>URAL</span></div>
    <div class="badge badge--organic"><span>ORG</span><span>ANIC</span></div>
    <div class="net-weight">500G</div>
    <div class="tagline"><span class="quote-mark">'</span><p>The healthy snack</p><p>that everyone craves</p><p>out-beyond meal time</p></div>
  </section>

  <section class="label label--mixed">
    <svg class="window" viewBox="0 0 347 339" role="img" aria-label="Die-cut window showing mixed nuts: cashews, almonds, hazelnuts and brazil nuts">
      <defs>
        <linearGradient id="mixed-fill" x1="0" y1="0" x2="1" y2="1">
          <stop offset="0" stop-color="#d9c6a4"/>
          <stop offset="0.45" stop-color="#a8693d"/>
          <stop offset="1" stop-color="#8c4f2b"/>
        </linearGradient>
      </defs>
      <polygon points="0,132 347,234 347,339 0,339" fill="url(#mixed-fill)"/>
    </svg>
    <div class="brand-mark"><span class="brand-mark__square"></span><span>Out-Beyond</span></div>
    <div class="grade">PREMIUM</div>
    <h2 class="product-name">Mixed Nuts</h2>
    <div class="badge badge--healthy"><span>HEA</span><span>LTHY</span></div>
    <div class="badge badge--natural"><span>NAT</span><span>URAL</span></div>
    <div class="badge badge--organic"><span>ORG</span><span>ANIC</span></div>
    <div class="net-weight">500G</div>
    <div class="tagline"><span class="quote-mark">'</span><p>The healthy snack</p><p>that everyone craves</p><p>out-beyond meal time</p></div>
  </section>

  <section class="label label--fruits">
    <svg class="window" viewBox="0 0 347 339" role="img" aria-label="Die-cut window showing dried fruit muesli with oats, raisins, seeds and blueberries">
      <defs>
        <linearGradient id="fruits-fill" x1="0" y1="0" x2="1" y2="1">
          <stop offset="0" stop-color="#8e9098"/>
          <stop offset="0.45" stop-color="#cbb994"/>
          <stop offset="1" stop-color="#b8a57f"/>
        </linearGradient>
      </defs>
      <polygon points="0,132 347,234 347,339 0,339" fill="url(#fruits-fill)"/>
    </svg>
    <div class="brand-mark"><span class="brand-mark__square"></span><span>Out-Beyond</span></div>
    <div class="grade">PREMIUM</div>
    <h2 class="product-name">Dried Fruits</h2>
    <div class="badge badge--healthy"><span>HEA</span><span>LTHY</span></div>
    <div class="badge badge--natural"><span>NAT</span><span>URAL</span></div>
    <div class="badge badge--organic"><span>ORG</span><span>ANIC</span></div>
    <div class="net-weight">500G</div>
    <div class="tagline"><span class="quote-mark">'</span><p>The healthy snack</p><p>that everyone craves</p><p>out-beyond meal time</p></div>
  </section>

  <section class="label label--peanuts">
    <svg class="window" viewBox="0 0 347 339" role="img" aria-label="Die-cut window showing roasted nuts inside the jar">
      <defs>
        <linearGradient id="peanuts-fill" x1="0" y1="0" x2="1" y2="1">
          <stop offset="0" stop-color="#d9c6a4"/>
          <stop offset="0.45" stop-color="#a8693d"/>
          <stop offset="1" stop-color="#8c4f2b"/>
        </linearGradient>
      </defs>
      <polygon points="0,132 347,234 347,339 0,339" fill="url(#peanuts-fill)"/>
    </svg>
    <div class="brand-mark"><span class="brand-mark__square"></span><span>Out-Beyond</span></div>
    <div class="grade">PREMIUM</div>
    <h2 class="product-name">Peanuts</h2>
    <div class="badge badge--healthy"><span>HEA</span><span>LTHY</span></div>
    <div class="badge badge--natural"><span>NAT</span><span>URAL</span></div>
    <div class="badge badge--organic"><span>ORG</span><span>ANIC</span></div>
    <div class="net-weight">500G</div>
    <div class="tagline"><span class="quote-mark">'</span><p>The healthy snack</p><p>that everyone craves</p><p>out-beyond meal time</p></div>
  </section>

</main>
</body>
</html>
```